Stationary For Harbor Allies
Harbor Allies
Project: Stationary For Harbor Allies
Stationary For Harbor Allies - Consulting
Creative Brief
Professional
Lou Brannick
President
547 Marlow Ln Spring Branch, TX 78070
lbrannick@harborallies4.com
www.harborallies4.com
I will need letterhead and envelopes as well as business cards. Feel free to try different fonts.
quelnor42 quelnor42
Designers, Please focus more on the letterhead and envelopes than the business cards. Thanks!

```html
<!DOCTYPE html>
<html lang="en">
<head>
<meta charset="utf-8">
<title>Harbor Allies – Business Cards</title>
<link rel="stylesheet" href="https://fonts.googleapis.com/css2?family=Open+Sans:wght@400;600&display=swap">
<style>
  :root {
    --bg: #e9e7e3;
    --navy: #2f5489;
    --royal: #3266b0;
    --card-white: #fdfdfd;
    --card-grey: #e6e7e9;
    --swoosh: #a7aab0;
    --text-light: #ffffff;
  }
  * { margin: 0; padding: 0; box-sizing: border-box; }
  html, body { width: 1200px; height: 901px; overflow: hidden; }
  body {
    background: var(--bg);
    font-family: "Open Sans", Arial, sans-serif;
    position: relative;
  }
  .card {
    position: absolute;
    left: 280px;
    width: 640px;
    height: 366px;
    overflow: hidden;
    box-shadow: 0 8px 22px rgba(0,0,0,0.18);
  }
  .card-front {
    top: 50px;
    background: linear-gradient(135deg, var(--card-white) 0%, var(--card-grey) 100%);
  }
  .card-back {
    top: 470px;
    background: linear-gradient(135deg, var(--card-white) 40%, var(--card-grey) 100%);
  }
  .brand-dot {
    position: absolute;
    border-radius: 50%;
    background: var(--royal);
  }
  .brand-name {
    position: absolute;
    color: var(--royal);
    font-weight: 600;
    white-space: nowrap;
  }
  .card-front .brand-dot { left: 70px; top: 70px; width: 110px; height: 110px; }
  .card-front .brand-name { right: 60px; top: 172px; font-size: 54px; line-height: 1; }
  .card-back .brand-dot { left: 420px; top: 105px; width: 96px; height: 96px; }
  .card-back .brand-name { right: 40px; top: 222px; font-size: 28px; line-height: 1; }
  .back-panel { position: absolute; inset: 0; }
  .holder {
    position: absolute;
    left: 40px;
    top: 70px;
    color: var(--text-light);
  }
  .holder-name { font-size: 22px; font-weight: 600; line-height: 1.2; }
  .holder-title { font-size: 16px; font-weight: 400; }
  .contact-list {
    position: absolute;
    left: 40px;
    top: 190px;
    list-style: none;
    color: var(--text-light);
    font-size: 12.5px;
    line-height: 20px;
  }
  .contact-list li { display: flex; align-items: center; gap: 9px; }
  .contact-list .address { margin-bottom: 10px; align-items: flex-start; max-width: 190px; line-height: 17px; }
  .icon {
    width: 14px; height: 14px; flex: none;
    border-radius: 50%;
    background: var(--text-light);
    display: flex; align-items: center; justify-content: center;
  }
  .icon svg { width: 9px; height: 9px; fill: var(--navy); }
</style>
</head>
<body>

<section class="card card-front" aria-label="Business card front">
  <span class="brand-dot"></span>
  <span class="brand-name">Harbor Allies</span>
</section>

<section class="card card-back" aria-label="Business card back">
  <svg class="back-panel" viewBox="0 0 640 366" preserveAspectRatio="none" aria-hidden="true">
    <path d="M0 0 H300 C230 90 225 250 305 366 H0 Z" fill="var(--navy)"/>
    <path d="M300 0 C230 90 225 250 305 366 H318 C240 250 246 90 318 0 Z" fill="var(--swoosh)" opacity="0.55"/>
  </svg>

  <div class="holder">
    <p class="holder-name">Lou Brannick</p>
    <p class="holder-title">President</p>
  </div>

  <ul class="contact-list">
    <li class="address">
      <span class="icon"><svg viewBox="0 0 10 10"><path d="M5 0.5a3 3 0 0 0-3 3c0 2.3 3 6 3 6s3-3.7 3-6a3 3 0 0 0-3-3zm0 4.2a1.2 1.2 0 1 1 0-2.4 1.2 1.2 0 0 1 0 2.4z"/></svg></span>
      <span>547 Marlow Ln Spring Branch, TX 78070</span>
    </li>
    <li>
      <span class="icon"><svg viewBox="0 0 10 10"><path d="M2.2 0.8l1.6 1.9-0.9 1.1c0.6 1.3 1.6 2.3 2.9 2.9l1.1-0.9 1.9 1.6-0.9 1.6C4.4 8.9 1.1 5.6 0.6 1.7z"/></svg></span>
      <span>555-014-2231</span>
    </li>
    <li>
      <span class="icon"><svg viewBox="0 0 10 10"><path d="M2.2 0.8l1.6 1.9-0.9 1.1c0.6 1.3 1.6 2.3 2.9 2.9l1.1-0.9 1.9 1.6-0.9 1.6C4.4 8.9 1.1 5.6 0.6 1.7z"/></svg></span>
      <span>555-014-2232</span>
    </li>
    <li>
      <span class="icon"><svg viewBox="0 0 10 10"><path d="M2.2 0.8l1.6 1.9-0.9 1.1c0.6 1.3 1.6 2.3 2.9 2.9l1.1-0.9 1.9 1.6-0.9 1.6C4.4 8.9 1.1 5.6 0.6 1.7z"/></svg></span>
      <span>555-014-2233</span>
    </li>
    <li>
      <span class="icon"><svg viewBox="0 0 10 10"><path d="M1 2.5h8v5H1z M1 2.5l4 3 4-3" fill="none" stroke="var(--navy)" stroke-width="1.1"/></svg></span>
      <span>lbrannick@harborallies4.com</span>
    </li>
    <li>
      <span class="icon"><svg viewBox="0 0 10 10"><circle cx="5" cy="5" r="3.8" fill="none" stroke="var(--navy)" stroke-width="1"/><path d="M1.2 5h7.6M5 1.2c-2 2.2-2 5.4 0 7.6M5 1.2c2 2.2 2 5.4 0 7.6" fill="none" stroke="var(--navy)" stroke-width="0.8"/></svg></span>
      <span>www.harborallies4.com</span>
    </li>
  </ul>

  <span class="brand-dot"></span>
  <span class="brand-name">Harbor Allies</span>
</section>

</body>
</html>
```